HAIR EXTENSIONS

We need a web design for a company base in Chicago called Extensions by Corvella. We sale 100% human hair in Brazilian body wave deep wave straight or natural curl, Peruvian body wave straight or deep wave. Malaysian loose straight or body wave, in the chicago land.
We also ship hair to any city or country. We like to see design that use the colors pinks & grays, or would just like to see some design creative with colors thats inviting.

Also I'm using the quillmoss template, Home- banner contact us, about us, Features- product side/left sidebar, Shop- wish list /shopping cart/ tracking your order / checkout/ order received.
Porfolio-filterable 4column portfolio
Blog. Buy now

Industry/Entity Type

Hair

Number of Pages Required

4 page

Colors
aaaaaa
606060
dddddd
eea4c8
d3a5cc
b868aa
a6459a
ffc213
1b1b1b

Requirements
Must have
• I NEED THE DESIGNER TO DO THE 4 PAGE LIKE THIS.
• 1.HOME-PAGE BANNER CONTACT US SOME PRODUCT WITH SIDING IMAGES OF THE TOP PROUDCT
• 2.PRODUCT WITH SHOPPING CART- I WANT SIDING BARS FOR PRODUCT & SHOPPING CART WITH TRACKING YOUR ORDERS CHECK OUT & ORDER RECEIVED.
• 3.PORFOLIO PHOTO-I WANT A FEATURES FOR CUSTOMERS TO UPLOAN THERE PICTURE & BLOG ON THE PAGE
• 4.ABOUT US- TALK ABOUT ARE COMPAMY.
Nice to have
• hello designer
• I was working with a web developer for my site be for i came to pixelharborr & they build a site for me that i liked, You all can view it at www.Extensionsbycorvella.info
• long story short never could get them to finish the project after they got paid!!
• I know, why paid before its finish bad decision. So know I'm here starting over with you all.
• here is a list of my competition site
• www.lockshaventress.com
• www.velmatrade.com
• www.orlitasparlor.com
• So just to give some insight, I'm looking for something like the one i had builded.

```html
<!DOCTYPE html>
<html lang="en">
<head>
<meta charset="utf-8">
<title>Extensions by Corvella</title>
<link href="https://fonts.googleapis.com/css2?family=Open+Sans:wght@400;600;700&family=Oswald:wght@300;400&family=Raleway:wght@300;400&display=swap" rel="stylesheet">
<style>
:root{
  --pink:#e3186f;
  --ink:#1b1b1b;
  --dark:#262626;
  --grey:#606060;
  --mid:#aaaaaa;
  --line:#dddddd;
  --soft:#f3f3f3;
  --card:#e9e9ee;
  --white:#ffffff;
}
*{box-sizing:border-box;margin:0;padding:0}
html,body{width:810px;height:1200px;overflow:hidden}
body{position:relative;background:var(--white);font-family:"Open Sans",Arial,sans-serif;color:var(--grey)}
a{color:inherit;text-decoration:none}
.abs{position:absolute}

/* hero */
.hero{left:0;top:0;width:810px;height:272px;background:linear-gradient(100deg,#1a1a1a 0%,#3a3a3a 28%,#2a2a2a 45%,#5a5a5a 70%,#2b2b2b 100%)}
.topbar{left:113px;top:7px;font-size:7.5px;color:#bbb;display:flex;gap:5px}
.topbar span.sep{color:#777}
.social{right:112px;top:7px;display:flex;gap:7px}
.social i{display:block;width:8px;height:8px;border-radius:50%;background:#d0d0d0}
.header-box{left:114px;top:34px;width:584px;height:84px;border:1px solid rgba(255,255,255,.85);background:rgba(0,0,0,.35)}
.address{left:9px;top:22px;font-size:6.8px;line-height:11px;color:#e8e8e8;text-transform:uppercase}
.logo{left:0;width:100%;top:18px;text-align:center;font-family:"Raleway",sans-serif;font-weight:300;font-size:22px;letter-spacing:1px;color:var(--white)}
.account{right:13px;top:21px;width:62px;height:16px;border:1px solid #ccc;font-size:6.5px;color:#fff;display:flex;align-items:center;justify-content:center}
.nav{left:11px;top:66px;display:flex;font-family:"Oswald",sans-serif;font-size:7.5px;letter-spacing:.6px;color:#bbb}
.nav a{margin-right:0}
.nav a.active{color:#fff}
.cart{left:513px;top:60px;display:flex;align-items:center;gap:4px;color:#fff;font-size:7px;font-weight:700}
.cart small{display:block;font-size:4.5px;font-weight:400}
.search{left:559px;top:58px;width:22px;height:22px;border-left:1px solid #aaa;display:flex;align-items:center;justify-content:center}
.hero-copy{right:112px;top:158px;text-align:right;color:#fff}
.hero-copy h1{font-family:"Oswald",sans-serif;font-weight:400;font-size:19.5px;line-height:19.5px}
.hero-copy p{margin-top:9px;font-family:"Oswald",sans-serif;font-weight:300;font-size:7.6px;line-height:11px}

/* promos */
.promo{top:287px;width:180px;height:87px;background:var(--dark);border:1px solid #ccc;overflow:hidden}
.promo .photo{position:absolute;right:0;top:0;width:95px;height:100%;background:linear-gradient(90deg,#2a2a2a,#6b3b30 55%,#3a2523)}
.promo .copy{position:absolute;left:14px;top:5px;color:#fff;font-family:"Raleway",sans-serif}
.promo .big{font-size:21px;font-weight:300;line-height:24px;letter-spacing:.5px}
.promo .mid{font-size:12px;line-height:15px}
.promo .note{font-size:5.5px;line-height:8px;color:#888;font-family:"Open Sans",sans-serif;margin-top:2px}
.promo .pinknote{font-size:6.5px;color:var(--pink);margin-top:2px}
.promo .pct{font-size:13px;color:var(--pink)}
.promo .pct small{font-size:5px;writing-mode:vertical-rl;transform:rotate(180deg);display:inline-block;vertical-align:middle}
.btn-buy{position:absolute;left:14px;bottom:8px;border:1px solid #ccc;color:#fff;font-size:6px;padding:2px 7px}

/* sidebar */
.side-title{font-size:9.5px;color:var(--pink);border-top:2px solid var(--line);padding:5px 7px 0;width:127px;position:relative}
.side-title::before{content:"";position:absolute;left:0;top:-2px;width:45px;height:2px;background:var(--mid)}
.brands{left:113px;top:388px;width:127px}
.brands ul{list-style:none;margin-top:6px}
.brands li{height:17.1px;background:var(--soft);border-bottom:1px solid #cfcfcf;font-size:6.3px;color:#333;padding:5px 10px 0}
.blog{left:113px;top:646px;width:127px;height:138px;border:1px solid var(--line)}
.blog .side-title{border-top:none;padding-top:6px;font-size:10px;margin-left:2px}
.blog .side-title::before{left:-2px;top:0;width:45px;background:var(--mid)}
.post{display:flex;gap:4px;padding:3px 8px 0}
.post .thumb{width:21px;height:32px;background:linear-gradient(160deg,#c98a5e,#5a3025)}
.post p{font-size:5.8px;line-height:11px}
.post .pt{color:var(--pink)}
.post .by{font-style:italic;font-size:5px}
.sale-box{left:113px;top:802px;width:127px;height:179px;background:radial-gradient(circle at 50% 45%,#5a3036,#2a1416 70%)}
.sale-box .up{position:absolute;left:8px;top:63px;color:#fff;font-family:"Raleway",sans-serif;font-style:italic;font-size:30px}
.sale-box .up small{font-size:11px;color:var(--pink)}
.sale-box .off{position:absolute;right:6px;top:50px;color:var(--pink);font-size:7px;transform:rotate(-60deg)}
.sale-box .huge{position:absolute;left:0;width:100%;top:128px;text-align:center;font-family:"Oswald",sans-serif;font-size:18px;letter-spacing:2px;color:#ccc}

/* products */
.section-title{left:258px;width:440px;border-top:2px solid var(--line);font-size:9px;color:var(--pink);padding-top:5px}
.section-title::before{content:"";position:absolute;left:0;top:-2px;width:92px;height:2px;background:var(--mid)}
.grid{left:258px;width:440px;display:grid;grid-template-columns:repeat(4,104px);gap:8px}
.product{height:172px;border:1px solid #e3e3e3;text-align:center}
.product .image{height:116px;background:var(--card);display:flex;align-items:center;justify-content:center}
.product .image i{display:block;width:70px;height:60px;border-radius:40%}
.product h3{font-size:6.3px;font-weight:600;color:#222;margin-top:8px}
.product .price{font-size:6.5px;color:#222;margin-top:5px}
.product .price span{color:var(--pink)}
.add{display:inline-block;margin-top:10px;border:1px solid #ccc;font-size:5.5px;color:#777;padding:3px 7px}
.add.hot{background:var(--pink);border-color:var(--pink);color:#fff}

/* footer */
.footer{left:0;top:996px;width:810px;height:104px;background:var(--soft)}
.fcol{top:13px}
.fcol h4{font-size:8.5px;font-weight:600;color:var(--pink);border-bottom:1px solid var(--line);padding-bottom:3px;width:105px}
.fcol ul{list-style:none;margin-top:4px}
.fcol li{font-size:6px;line-height:15.2px;color:#444}
.fcol li::before{content:"»";color:var(--pink);margin-right:4px}
.fcol li.on{color:var(--pink)}
.fcol p{font-size:6px;line-height:10.6px;color:#444;margin-top:5px;width:110px}
.sub{margin-top:9px;display:flex}
.sub input{width:90px;height:16px;border:1px solid #ccc;font-size:5.5px;padding-left:5px;font-family:inherit;color:#aaa}
.sub b{width:20px;height:16px;background:var(--pink);color:#fff;font-size:7px;display:flex;align-items:center;justify-content:center}
.contacts{left:0;top:1100px;width:810px;height:68px}
.ci{top:14px;display:flex;gap:6px;border-bottom:1px solid var(--line);padding-bottom:8px}
.ci h5{font-size:8.5px;font-weight:400;color:var(--pink)}
.ci p{font-size:6px;line-height:9px;color:#444}
.bottom{left:0;top:1168px;width:810px;height:32px;background:var(--pink)}
.bottom p{position:absolute;left:113px;top:12px;font-size:6px;color:#fff}
.cards{position:absolute;left:569px;top:9px;display:flex;gap:5px}
.cards i{display:block;width:18px;height:13px;border-radius:2px;background:#fff}
</style>
</head>
<body>

<section class="hero abs" role="img" aria-label="Hero photo of a woman in profile with long flowing dark hair">
</section>
<div class="topbar abs"><a>Wish List</a><span class="sep">|</span><a>Shopping cart</a><span class="sep">|</span><a>Tracking your order</a><span class="sep">|</span><a>Checkout</a><span class="sep">|</span><a>Order Received</a></div>
<div class="social abs"><i></i><i></i><i></i><i></i><i></i><i></i></div>

<header class="header-box abs">
  <div class="address abs">Street No.412 Lakeview Row, Chicago, 60614<br>contact@corvellahair.com</div>
  <div class="logo abs">CORVELLA</div>
  <div class="account abs">⌄&nbsp; MY ACCOUNT</div>
  <nav class="nav abs">
    <a class="active" style="width:42px">HOME</a><a style="width:58px">ABOUT US</a><a style="width:80px">HAIR SOLUTIONS</a><a style="width:60px">PRODUCTS</a><a style="width:42px">SHOP</a><a style="width:65px">ORDER NOW</a><a style="width:41px">BLOG</a><a>CONTACT US</a>
  </nav>
  <div class="cart abs">
    <svg width="12" height="14" viewBox="0 0 12 14"><path d="M1 4h10v9H1z M4 4V2.5a2 2 0 0 1 4 0V4" fill="none" stroke="#fff" stroke-width="1.2"/></svg>
    <div>$0.00<small>0 items</small></div>
  </div>
  <div class="search abs">
    <svg width="12" height="12" viewBox="0 0 12 12"><circle cx="5" cy="5" r="3.8" fill="none" stroke="#fff" stroke-width="1.3"/><path d="M8 8l3.2 3.2" stroke="#fff" stroke-width="1.5"/></svg>
  </div>
</header>

<div class="hero-copy abs">
  <h1>GET EVERYTHING YOU NEED FOR<br>HAIR EXTENSION!</h1>
  <p>LOREM IPSUM DOLOR SIT AMET, CONSECTETUR ADIPISCING ELT AUCTOR<br>STO AT, VULPUTATE AUGUE. ETIAM&nbsp; AMET</p>
</div>

<article class="promo abs" style="left:113px">
  <div class="photo" role="img" aria-label="Model with auburn wavy hair"></div>
  <div class="copy"><div class="big">EXTRA</div><div class="mid">SALE</div><div class="pct"><small>OFF</small>50%</div></div>
  <a class="btn-buy">BUY NOW</a>
</article>
<article class="promo abs" style="left:315px">
  <div class="photo" role="img" aria-label="Model with dark curly wig" style="background:linear-gradient(90deg,#2a2a2a,#4a3a30 55%,#2b2220)"></div>
  <div class="copy"><div class="big">HIGH</div><div class="mid" style="font-size:10px">QUALITY WIGS</div><div class="note">BECOME ANOTHER YOU<br>IN MINUTES</div></div>
  <a class="btn-buy">BUY NOW</a>
</article>
<article class="promo abs" style="left:518px">
  <div class="photo" role="img" aria-label="Model with voluminous red curls" style="background:linear-gradient(90deg,#2a2a2a,#8a3d2e 55%,#4a2420)"></div>
  <div class="copy"><div class="big">HAIR</div><div class="mid" style="font-size:10.5px">EXTENSIONS</div><div class="pinknote">EXTEND YOUR BEAUTY</div></div>
  <a class="btn-buy">BUY NOW</a>
</article>

<aside class="brands abs">
  <h2 class="side-title">BRAND</h2>
  <ul>
    <li>Avenmoor Hair Extensions</li><li>Sollaine</li><li>Petra Lune</li><li>Silkwell Pro</li><li>Braevin</li><li>Fine Strands</li><li>Tressio</li><li>Lumaweave</li><li>Corlocks</li><li>WeaveNest</li><li>Brisa Hair Extensions</li><li>Velano USA</li><li>Maritress</li>
  </ul>
</aside>

<aside class="blog abs">
  <h2 class="side-title">BLOG</h2>
  <div class="post"><div class="thumb" role="img" aria-label="Blog thumbnail"></div><p><span class="pt">Lorem ipsum dolor sit</span><br>Lorem in tempus mic<br><span class="by">Post by Admin monday</span></p></div>
  <div class="post"><div class="thumb" role="img" aria-label="Blog thumbnail"></div><p><span class="pt">Lorem ipsum dolor sit</span><br>Lorem in tempus mio<br><span class="by">Post by Admin monday</span></p></div>
  <div class="post"><div class="thumb" role="img" aria-label="Blog thumbnail"></div><p><span class="pt">Lorem ipsum dolor sit</span><br>Lorem in tempus min<br><span class="by">Post by Admin monday</span></p></div>
</aside>

<aside class="sale-box abs" role="img" aria-label="Sale banner photo of a model with dark hair">
  <div class="up"><small>UP TO </small>50%</div>
  <div class="off">OFF</div>
  <div class="huge">HUGE SALE</div>
</aside>

<h2 class="section-title abs" style="top:389px">FEATURED PRODUCTS</h2>
<div class="grid abs" style="top:414px">
  <div class="product"><div class="image" role="img" aria-label="Black hair bow"><i style="background:#24262e;height:34px"></i></div><h3>BOW HAIR EXTENSION</h3><p class="price">$ 165.00 <span>(20% Off )</span></p><a class="add hot">ADD TO CART</a></div>
  <div class="product"><div class="image" role="img" aria-label="Blonde braided bun"><i style="background:#b59a6a;border-radius:50%;height:80px;width:80px"></i></div><h3>BOW HAIR EXTENSION</h3><p class="price">$ 165.00 <span>(20% Off )</span></p><a class="add">ADD TO CART</a></div>
  <div class="product"><div class="image" role="img" aria-label="Dark brown hair strand"><i style="background:linear-gradient(135deg,transparent 40%,#2a1a16 40%,#2a1a16 60%,transparent 60%)"></i></div><h3>BOW HAIR EXTENSION</h3><p class="price">$ 165.00 <span>(20% Off )</span></p><a class="add">ADD TO CART</a></div>
  <div class="product"><div class="image" role="img" aria-label="Copper hair strand"><i style="background:linear-gradient(135deg,transparent 40%,#9a5530 40%,#9a5530 60%,transparent 60%)"></i></div><h3>BOW HAIR EXTENSION</h3><p class="price">$ 165.00 <span>(20% Off )</span></p><a class="add">ADD TO CART</a></div>
  <div class="product"><div class="image" role="img" aria-label="Light brown hair bow comb"><i style="background:#d09a6c;height:40px"></i></div><h3>BOW HAIR EXTENSION</h3><p class="price">$ 165.00 <span>(20% Off )</span></p><a class="add">ADD TO CART</a></div>
  <div class="product"><div class="image" role="img" aria-label="Brown braided bun"><i style="background:#8a5a38;border-radius:50%;height:78px;width:78px"></i></div><h3>BOW HAIR EXTENSION</h3><p class="price">$ 165.00 <span>(20% Off )</span></p><a class="add">ADD TO CART</a></div>
  <div class="product"><div class="image" role="img" aria-label="Auburn clip-in weft"><i style="background:#8a3d22;width:26px;height:90px;border-radius:6px"></i></div><h3>BOW HAIR EXTENSION</h3><p class="price">$ 165.00 <span>(20% Off )</span></p><a class="add">ADD TO CART</a></div>
  <div class="product"><div class="image" role="img" aria-label="Blonde keratin tip bundle"><i style="background:linear-gradient(#8a6a40,#e0c08a);width:28px;height:90px;border-radius:6px"></i></div><h3>BOW HAIR EXTENSION</h3><p class="price">$ 165.00 <span>(20% Off )</span></p><a class="add">ADD TO CART</a></div>
</div>

<h2 class="section-title abs" style="top:784px">LATEST PRODUCTS</h2>
<div class="grid abs" style="top:809px">
  <div class="product"><div class="image" role="img" aria-label="Black hair bow"><i style="background:#24262e;height:34px"></i></div><h3>BOW HAIR EXTENSION</h3><p class="price">$ 165.00 <span>(20% Off )</span></p><a class="add">ADD TO CART</a></div>
  <div class="product"><div class="image" role="img" aria-label="Blonde braided bun"><i style="background:#b59a6a;border-radius:50%;height:80px;width:80px"></i></div><h3>BOW HAIR EXTENSION</h3><p class="price">$ 165.00 <span>(20% Off )</span></p><a class="add">ADD TO CART</a></div>
  <div class="product"><div class="image" role="img" aria-label="Dark brown hair strand"><i style="background:linear-gradient(135deg,transparent 40%,#2a1a16 40%,#2a1a16 60%,transparent 60%)"></i></div><h3>BOW HAIR EXTENSION</h3><p class="price">$ 165.00 <span>(20% Off )</span></p><a class="add">ADD TO CART</a></div>
  <div class="product"><div class="image" role="img" aria-label="Copper hair strand"><i style="background:linear-gradient(135deg,transparent 40%,#9a5530 40%,#9a5530 60%,transparent 60%)"></i></div><h3>BOW HAIR EXTENSION</h3><p class="price">$ 165.00 <span>(20% Off )</span></p><a class="add">ADD TO CART</a></div>
</div>

<footer class="footer abs">
  <div class="fcol abs" style="left:113px"><h4>NEVIGATION</h4><ul><li class="on">Home</li><li>About us</li><li>Hair solutions</li><li>Shop</li><li>Contact us</li></ul></div>
  <div class="fcol abs" style="left:251px"><h4>ABOUT US</h4><ul><li>Shipping &amp; Delivery</li><li>Guarantee/Return Policy</li><li>Privacy &amp; Security Policy</li><li>Hair Extensions&nbsp; Story</li><li>Career Opportunities</li></ul></div>
  <div class="fcol abs" style="left:417px"><h4>SHOPPING SERVICES</h4><ul><li>Access My Account</li><li>Check Order Status</li><li>Hair Extensions Credit Card Bill</li><li>Buy Gift Cards</li><li>Place Catalog Order</li></ul></div>
  <div class="fcol abs" style="left:589px"><h4>NEWSLETTER SINGUP</h4><p>Lorem ipsum dolor sit amet, ctetur adipisicing elit, sed do eiusm mpor incididunt ut labore et dolore amet magna aliqua.</p><div class="sub"><input value="Email" aria-label="Email"><b>GO</b></div></div>
</footer>

<section class="contacts abs">
  <div class="ci abs" style="left:113px;width:110px">
    <svg width="22" height="20" viewBox="0 0 22 20"><path d="M1 7l10-6 10 6v12H1z" fill="none" stroke="#222" stroke-width="1.5"/><path d="M1 7l10 7 10-7" fill="none" stroke="#222" stroke-width="1.5"/></svg>
    <div><h5>Email</h5><p>hello@corvellahair.com</p></div>
  </div>
  <div class="ci abs" style="left:267px;width:134px">
    <svg width="20" height="20" viewBox="0 0 20 20"><path d="M10 2a4 4 0 0 1 4 4c0 3-4 7-4 7s-4-4-4-7a4 4 0 0 1 4-4z" fill="none" stroke="#222" stroke-width="1.5"/><circle cx="10" cy="6" r="1.3" fill="#222"/><path d="M1 18l4-5h10l4 5z" fill="none" stroke="#222" stroke-width="1.3"/></svg>
    <div><h5>Hair Extensions Shop Location</h5><p>Lorem Ispum Dolar sit<br>Chicago, IL - 60614</p></div>
  </div>
  <div class="ci abs" style="left:454px;width:74px">
    <svg width="20" height="20" viewBox="0 0 20 20" fill="#222"><circle cx="4" cy="5" r="1.6"/><circle cx="10" cy="5" r="1.6"/><circle cx="16" cy="5" r="1.6"/><circle cx="4" cy="10" r="1.6"/><circle cx="10" cy="10" r="1.6"/><circle cx="16" cy="10" r="1.6"/><circle cx="4" cy="15" r="1.6"/><circle cx="10" cy="15" r="1.6"/><circle cx="16" cy="15" r="1.6"/></svg>
    <div><h5>Call Us</h5><p>312-555-0148</p></div>
  </div>
  <div class="ci abs" style="left:579px;width:119px">
    <svg width="20" height="22" viewBox="0 0 20 22"><circle cx="10" cy="12" r="8" fill="none" stroke="#222" stroke-width="1.6"/><path d="M8 2h4M10 2v2M10 12V7M10 12l3 2" stroke="#222" stroke-width="1.5" fill="none"/></svg>
    <div><h5>Working Hours</h5><p>Monday to Friday from<br>9: 30-12: 30 and 14: 00-18: 30</p></div>
  </div>
</section>

<div class="bottom abs">
  <p>Copyright&nbsp; 2014 hair extensions | All rights reserved.</p>
  <div class="cards"><i></i><i></i><i></i><i></i><i></i><i></i></div>
</div>

</body>
</html>
```